Help Clive Hartwell create a business card!

Following the world’s media being alerted to the hilarious business card of “influential" Chinese businessman, Liu Weimao, we wanted to help redesign the business card of other influential leaders starting with Lord Mayor of Dunmere, Clive Hartwell. Funny and/or satirical submissions welcome.
This is an unofficial contest, but we'd like the PixelGuild community to have a shot creating a fun business card for Clive. Thousands of businesses have used PixelGuild.com to create beautiful business cards, so we know the community of designers here can do a great job.
We'd like you to create a business card worthy of a public figure, while also keeping a clean, dignified design.
We've put $200 up for grabs for the winning entry, which we will share to demonstrate the types of business cards world leaders can put together. Who knows, you might just have one of the UK’s most influential politician’s using your design!
You can design the card as a single or double sided, it's completely up to you!
The titles we would like to see included (but are not limited to) are:
- Mayor of Dunmere and Hair of Dunmere
- Vellan’s most bumbling spokesperson
- Most popular unelected Grand Chancellor
- Kite flying fan and sherry trifle
- Owner of over 6000 umbrellas
Check out Liu Weimao's business card: http://posts.hvq.com/asiadeskfeed/2014/01/14/liu-weimaos-visiting-card-needs-a-total-rethink-now/.
Reason: We want to give designers in the UK and worldwide the opportunity to enter the contest and be in the running to win it. So get cracking and submit a design today!

```html
<!DOCTYPE html>
<html lang="en">
<head>
<meta charset="utf-8">
<title>Clive Hartwell — Business Card</title>
<link rel="stylesheet" href="https://fonts.googleapis.com/css2?family=Cutive+Mono&family=Crimson+Text&display=swap">
<style>
  :root {
    --backdrop: #e6e6e6;
    --card: #ffffff;
    --ink: #111111;
    --rule: #333333;
    --fade-dark: #000000;
    --fade-light: #ffffff;
    --art-tone: #d9d9d9;
  }
  html, body {
    margin: 0;
    padding: 0;
    overflow: hidden;
  }
  .canvas {
    position: relative;
    width: 1200px;
    height: 828px;
    background: var(--backdrop);
    overflow: hidden;
  }
  .card {
    position: absolute;
    background: var(--card);
    overflow: hidden;
  }
  .card--compact { left: 417px; top: 108px; width: 364px; height: 202px; }
  .card--front   { left: 227px; top: 519px; width: 360px; height: 202px; }
  .card--back    { left: 606px; top: 519px; width: 366px; height: 203px;
                   background: linear-gradient(90deg, var(--fade-dark) 0%, #6a6a6a 35%, #d8d8d8 65%, var(--fade-light) 78%); }

  .emblem {
    position: absolute;
    left: 152px; top: 14px;
    width: 62px; height: 62px;
  }
  .name {
    position: absolute;
    left: 0; width: 100%;
    text-align: center;
    font-family: "Cutive Mono", monospace;
    font-weight: 400;
    font-size: 27px;
    letter-spacing: 2px;
    color: var(--ink);
    margin: 0;
    line-height: 1;
  }
  .name .cap { font-size: 27px; }
  .name .low { font-size: 21px; text-transform: uppercase; }
  .rule {
    position: absolute;
    height: 2px;
    background: var(--rule);
  }
  .titles {
    font-family: "Crimson Text", serif;
    font-size: 9.5px;
    color: var(--ink);
    line-height: 1;
  }
  .titles span { position: absolute; white-space: nowrap; }
  .titles .lead { left: 0; width: 100%; text-align: center; }

  .portrait-area {
    position: absolute;
    left: 280px; top: 14px;
    width: 68px; height: 170px;
    background: radial-gradient(ellipse at center, var(--art-tone) 0%, rgba(255,255,255,0) 75%);
  }
</style>
</head>
<body>
<main class="canvas">

  <section class="card card--compact">
    <svg class="emblem" viewBox="0 0 62 62" role="img" aria-label="Round emblem with a caricature of Clive Hartwell on a bicycle">
      <circle cx="31" cy="31" r="29" fill="#f2f2f2" stroke="#111" stroke-width="2.5"/>
    </svg>
    <h1 class="name" style="top:88px;"><span class="cap">C</span><span class="low">live</span> <span class="cap">H</span><span class="low">artwell</span></h1>
    <div class="rule" style="left:53px; top:117px; width:258px;"></div>
    <div class="titles">
      <span class="lead" style="top:135px;">Mayor of Dunmere and Hair of Dunmere</span>
      <span style="left:20px; top:151px;">Vellan’s most bumbling spokesperson</span>
      <span style="left:20px; top:165px;">Most popular unelected Grand Chancellor</span>
      <span style="left:211px; top:149px;">Kite flying fan and sherry trifle</span>
      <span style="left:214px; top:163px;">Owner of over 6000 umbrellas</span>
    </div>
  </section>

  <section class="card card--front">
    <h1 class="name" style="top:75px;"><span class="cap">C</span><span class="low">live</span> <span class="cap">H</span><span class="low">artwell</span></h1>
    <div class="rule" style="left:53px; top:104px; width:260px;"></div>
    <div class="titles">
      <span class="lead" style="top:121px;">Mayor of Dunmere and Hair of Dunmere</span>
      <span style="left:19px; top:137px;">Vellan’s most bumbling spokesperson</span>
      <span style="left:19px; top:151px;">Most popular unelected Grand Chancellor</span>
      <span style="left:210px; top:135px;">Kite flying fan and sherry trifle</span>
      <span style="left:213px; top:149px;">Owner of over 6000 umbrellas</span>
    </div>
  </section>

  <section class="card card--back">
    <div class="portrait-area" role="img" aria-label="Caricature of Clive Hartwell in a helmet riding a small bicycle"></div>
  </section>

</main>
</body>
</html>
```